Guarenteed! - Homepage Website Design - Coding not required- Winner to complete further pages

Hi all,

We're looking at redesigning our current website with a few adjustments to other pages but the main adjustments will be on the homepage which is what this design request is for. Please note : any of these ideas can be changed if you have something particularly different / special in mind etc.

P.S Coding is not required, just a design.

- Our website -

Our website is simply a price comparison website that allows customers to find companies within their area at the best price. The products available are mostly related to the vehicle trade and all refer to vinyl. This includes the likes of vehicle window tint, vehicle colour change vehicle wrap, vehicle signage as well as other cosmetic vinyl modifications. We allow the customer to search for their product within their chosen area and receive a list of companies who supply their product within that area. From here they can compare prices and view further details on the company.

- What we're looking to do -

We're looking first of all to adjust how the website homepage is displayed, this includes adding images and adjusting the colours that are explained below:

First of all, we look to spread out each of the 12 products (which can be seen on the website as it stands) and add an image to each of the products (all being spaced out as shown in our sketch)

We've been told the website looks too busy so we're thinking if we adjust the colours to more simplier neutral colours as well as the main focus of the website being on the 12 images, that would be great.

- Logo + Banner -

Logo to remain top left although banner may be removed / adjusted to make simplier.

- Colours -

Adjustments - Colours shades
We want the website to still look exciting but simplify the colours. Needs to be kept up to date with the colours / textures etc (bright colours to highlight keypoints)
We're still looking to use either blue or orange or maybe both to highlight these keypoints but the main website to be light colours and maybe even black on white background. The entire homepage can be adjusted colour wise if you feel it fits into your theme including menu bars, banners etc. The key is to get this right with being not too overpowering with the colours but still look interesting and up to date.

- 1 - 4 steps banner - (text may change)

This sits just under the logo and explains to the user how easy the website is to use and the steps they need to take. This may change to a 1 - 5 steps but we're looking to have this designed once the overall colours / theme of the website is sorted.

- 12 images - 4 x 3

This is the main focus of the website and will be the main focus of what the customer sees first of all. This will be where they select their product and then underneath, enter their postcode and distance they would like to search within. As explained further up, we have some of the product images available so if you can where possible add these to the design and then duplicate the images on those we currently don't have available.

- 12 Images -Titles -

These titles will be in this order from left to right and etc

- Colour Change Wrap
- Printed Vehicle Wrap
- Window Tint
- Headlight Tint
- Vehicle Signage
- Shop Signage
- Roof Vinyl Wrap
- Bonnet Vinyl Wrap
- Carbon Fibre Vinyl
- Stickerbomb Vinyl
- Clear Protective Vinyl
- Wheel Refurb

Text to be quite large, centered and with the o to the left of the title. Short titles like 'Window Tint' should fit on one line in the middle of the box where as titles such as ' Stickerbomb Vinyl Wrap' should have the 'Stickerbomb Vinyl' on the first line with the 'Wrap' on the line below. The background of this text is up to experient, might be worth just a simple colour or it might be worth using a bright blue or orange to keep in with the theme of the logo etc.

These will also have the circle tick box to the left of the title (as on the current website) where the customer clicks to select the product they have available.
We were also thinking that if when the customer ticks the circle on their selected box, the box is highlighted in some way to show this.

- Search Block -

This will appear under the 12 images and allows the customer to input their postcode and distance for the search criteria. Colours on this can of course be adjusted to keep in theme with the website.

- Under the 12 Images -

- Block underneath the 12 images and search block -

To the left will be some key bullet points about the website - maybe 4 or 5 with a green tick to the left of this. Background colour will probably be best to be a light colour, possibly grey.

Then to the right of this will appear 4 images, 2 before and 2 after when applying these products. Images to be used aren't fully decided on and we would like this stage of the design left to the end when the rest of the theme etc have been decided on.

Attached images are as follows :
- How the website looks as it stands
- The fold line on the website (obviously important)
- Our rough sketch of how we'd like the website homepage to look.
- We have 7 of the images ready that are all attached in this one file. Please duplicate the images on those that currently don't have the image available.

We will also be requesting a website developer to put this into action if our current designer falls through so please feel free to contact us if potentially interested.

The layout can change if you can think of something particular different / unique that works with this design. The main idea is to not only get the 12 products on view to the viewers but also the keypoints and before and after images.

Any questions, please ask away as we're bound to have forgotten a few things.

Thanks and good luck!

Hi all, keep the designs coming.

We haven't quite seen that extra special design we're after. As stated, we're after something fairly simple to suit the youth as well as the middle aged but we're also after something that bit special.

Colours to concentrate on are still and orange etc although feel free to use other colours if you have anything special in mind.

Please experience and we'll give you our honest feedback.

Many thanks all and good luck!

Hi all, this is a message to all the designers.

Some good designs coming in but we're still after that something special for the website design. Keep the designs coming and please feel free to experiment with the design colours, layout etc.

The basic principle of the website needs to remain regarding the 12 products, search within block and 4 steps all appearing on the homepage.

The 4 steps seems to work best when it's got text as well as some simple images next to this.

A variation with the product titles with how to display this, some designers have gone with a simple white background whereas others have gone with colours. Please experiment here and where possible, add a contract / texture to the colour. Please remember the product titles needs to be clear, centured and with the circle tick box to the left of it. 

We're after a fairly simple design although we need it to look 21st century, up to date as well as interesting. The key points straight away are the 4 steps as well as the 12 products so try to guide the viewer to these areas a little.

White background behind the 12 images seems to be a much, although a light colour could possibly work.

The keypoints underneath these 12 products are too very important as it outlines what we do etc. Tick colour can vary.

Next to these keypoints will be the 'before' and 'after' images, these images needs to be fairly small and ensure there is white background around the image itself.

Good luck all and any questions, feel free to ask away.

Thanks!

Hi,

 Thank you for your time and effort with these designs, we are very nearly there with the design but we've thought of something that may work for the homepage. A curved arrow from step 1 pointing to the products, this may or may not work but feel free to give it a go.

Many thanks,

Thank you to everyone for your time and efforts with the design. It's hugely appreciated so thank you all once again.

Wish you all the luck in the future.

```html
<!DOCTYPE html>
<html lang="en">
<head>
<meta charset="utf-8">
<title>WrapMatch Fitters – Homepage</title>
<link href="https://fonts.googleapis.com/css2?family=Michroma&family=Open+Sans:wght@400;600;700&display=swap" rel="stylesheet">
<style>
:root{
  --navy:#34477a;
  --orange:#f09d38;
  --grey-bg:#f1f1f1;
  --ink:#1b1b1b;
  --text:#333;
  --white:#fff;
  --car-white:#f4f4f5;
  --car-shadow:#b9babd;
  --tyre:#2a2a2a;
}
*{box-sizing:border-box;margin:0;padding:0}
html,body{width:851px;height:1200px;overflow:hidden}
body{position:relative;background:var(--grey-bg);font-family:"Open Sans",Arial,sans-serif;color:var(--text)}
a{text-decoration:none}

/* Header */
.site-header{position:absolute;left:0;top:0;width:851px;height:129px;
  background:
    radial-gradient(circle at 12% 30%,rgba(90,110,150,.55) 0,transparent 30%),
    radial-gradient(circle at 85% 70%,rgba(150,120,80,.45) 0,transparent 30%),
    radial-gradient(circle at 60% 20%,rgba(70,120,110,.4) 0,transparent 25%),
    linear-gradient(180deg,#3a3d46 0%,#23262d 100%)}
.brand{position:absolute;left:160px;top:28px;display:flex;align-items:center;gap:8px}
.brand-dot{width:26px;height:26px;border-radius:50%;background:var(--orange)}
.brand-name{font-family:"Michroma",sans-serif;font-size:12px;color:var(--white);letter-spacing:1px;line-height:15px}
.cta-strip{position:absolute;left:442px;top:32px;display:flex;height:31px}
.cta-text{width:151px;background:#1d1f24;border:1px solid #555;color:var(--white);font-family:"Michroma",sans-serif;font-size:6.6px;line-height:10px;padding:5px 8px;letter-spacing:.3px;white-space:nowrap}
.cta-search{width:97px;background:var(--orange);color:var(--white);font-family:"Michroma",sans-serif;font-size:5.6px;line-height:6.5px;padding:6px 4px 0 28px;position:relative;letter-spacing:.4px}
.cta-search svg{position:absolute;left:7px;top:8px}
.main-nav{position:absolute;left:0;top:86px;width:851px;height:24px;border-top:1px solid rgba(255,255,255,.15);border-bottom:1px solid rgba(255,255,255,.15)}
.main-nav a{position:absolute;top:0;height:24px;line-height:24px;font-family:"Michroma",sans-serif;font-size:7px;color:var(--white);letter-spacing:1px;white-space:nowrap}
.main-nav a.active{left:158px;width:70px;text-align:center;background:var(--orange);clip-path:polygon(0 0,100% 0,92% 100%,8% 100%)}

/* Hero */
.hero{position:absolute;left:0;top:129px;width:851px;height:125px;background:var(--white);text-align:center}
.hero h1{font-family:"Michroma",sans-serif;font-size:18px;color:var(--ink);margin-top:26px;letter-spacing:1px}
.hero p{font-size:10.5px;line-height:13px;color:var(--ink);margin-top:4px}
.hero-btn{position:absolute;left:350px;top:83px;width:151px;height:24px;background:var(--navy);color:var(--white);
  font-family:"Michroma",sans-serif;font-size:8.5px;letter-spacing:2px;line-height:24px;clip-path:polygon(0 0,100% 0,96% 50%,100% 100%,0 100%,4% 50%)}
.hero-rule{position:absolute;top:95px;height:2px;width:24px;background:var(--navy)}

/* Steps */
.step{position:absolute;top:278px;width:128px;height:112px;background:var(--navy);color:var(--white);text-align:center;font-size:8.6px;line-height:10px}
.step svg{position:absolute;left:41px;top:20px}
.step-num{position:absolute;left:0;width:100%;top:29px;font-size:20px;line-height:28px;font-weight:300}
.step-label{position:absolute;left:0;width:100%;top:75px}

/* Products */
.product{position:absolute;width:128px}
.product-photo{width:128px;height:112px;border:1px solid #dcdcdc}
.photo-car{background:
  linear-gradient(90deg,#f2c230 0%,#e5432c 22%,#2f9d4a 40%,#f4e04d 55%,#2b6fc4 72%,#e5432c 88%,#f2c230 100%) 50% 42%/78% 30% no-repeat,
  linear-gradient(180deg,#f0f0f1 0%,#3b3b3d 10%,#3b3b3d 18%,var(--car-white) 62%,var(--car-shadow) 78%,var(--tyre) 86%,#e4e4e6 100%)}
.photo-store{background:linear-gradient(180deg,#e3e6e9 0%,#e3e6e9 14%,#2d2d2f 16%,#2d2d2f 78%,#d4d4d4 82%,#bdbdbd 100%)}
.photo-bonnet{background:radial-gradient(ellipse 55% 45% at 55% 50%,#3d3d3f 0%,#8a8a8c 45%,#d0d0d2 70%,#fff 100%)}
.photo-van{position:relative;background:linear-gradient(180deg,#2b2b2b 0%,#4a4a48 45%,#6d7a5a 70%,#1e1e1e 100%)}
.photo-van::before{content:"";position:absolute;right:0;top:0;border-left:16px solid transparent;border-top:16px solid var(--orange)}
.plus-h,.plus-v{position:absolute;background:var(--orange)}
.plus-h{left:48px;top:53px;width:32px;height:2px}
.plus-v{left:63px;top:38px;width:2px;height:32px}
.more{position:absolute;width:100%;top:75px;text-align:center;font-size:8px;color:var(--orange)}
.product-title{text-align:center;font-size:10.4px;color:var(--ink);margin-top:8px}

/* Help and before/after */
.help{position:absolute;left:158px;top:904px;width:237px;height:156px;background:var(--orange);color:var(--white);padding:21px 0 0 21px}
.help h2{font-family:"Michroma",sans-serif;font-size:9.4px;font-weight:400;letter-spacing:.6px;margin-bottom:12px}
.help li{list-style:none;position:relative;padding-left:18px;font-size:8.2px;line-height:10px;margin-bottom:10px;white-space:nowrap}
.help li svg{position:absolute;left:0;top:3px}
.ba{position:absolute;top:904px;width:144px;height:156px;background:var(--orange)}
.ba h3{font-family:"Michroma",sans-serif;font-weight:400;font-size:10px;color:var(--white);text-align:center;margin-top:14px;letter-spacing:1px}
.ba-arrow{position:absolute;top:18px;width:10px;height:10px;border-radius:50%;background:var(--white)}
.ba-arrow svg{display:block}
.ba-photo{position:absolute;left:8px;top:35px;width:129px;height:112px}
.ba-photo.before{background:
  linear-gradient(180deg,transparent 0%,transparent 22%,#f7f7f7 24%,#eeeeee 62%,#cfcfcf 70%,transparent 72%) 20% 0/90% 100% no-repeat,
  linear-gradient(180deg,#6f6a55 0%,#9c9579 30%,#8a8a86 72%,#5d5d5b 100%)}
.ba-photo.after{background:
  linear-gradient(100deg,#f3f3f3 0%,#e23b31 30%,#d02a2a 50%,#f08a2a 68%,#f4c03a 80%,#c92d2d 100%) 60% 50%/95% 60% no-repeat,
  linear-gradient(180deg,#b9bec4 0%,#9fa5ab 55%,#5f6266 100%)}
.click{position:absolute;top:1068px;font-family:"Michroma",sans-serif;font-size:10px;color:var(--navy);letter-spacing:1px}

/* Footer */
.mascot-spot{position:absolute;left:399px;top:1088px;width:54px;height:38px;border-radius:27px 27px 0 0;background:var(--orange)}
.site-footer{position:absolute;left:0;top:1125px;width:851px;height:75px;background:var(--navy);color:var(--white);text-align:center}
.social{display:flex;justify-content:center;gap:8px;margin-top:17px}
.social span{width:12px;height:12px;border-radius:50%;background:var(--white)}
.footer-links{font-size:6.6px;margin-top:8px;letter-spacing:.2px}
.copyright{font-size:6.4px;margin-top:3px}
</style>
</head>
<body>

<header class="site-header">
  <div class="brand">
    <span class="brand-dot"></span>
    <span class="brand-name">WRAPMATCH<br>FITTERS</span>
  </div>
  <div class="cta-strip">
    <div class="cta-text">FIND A PROFESSIONAL<br>VINYLE INSTALLER TODAY</div>
    <div class="cta-search">
      <svg width="15" height="15" viewBox="0 0 15 15"><circle cx="6" cy="6" r="4.5" fill="none" stroke="#fff" stroke-width="2"/><line x1="9.5" y1="9.5" x2="14" y2="14" stroke="#fff" stroke-width="2.4"/></svg>
      SEARCH<br>AND SAVE<br>IN SECONDS
    </div>
  </div>
  <nav class="main-nav">
    <a class="active" href="#">HOME</a>
    <a href="#" style="left:242px">BEGINNERS GUIDE</a>
    <a href="#" style="left:376px">BLOG</a>
    <a href="#" style="left:433px">CONTACT US</a>
    <a href="#" style="left:532px">LIST YOUR COMPANY HERE</a>
  </nav>
</header>

<section class="hero">
  <h1>LOREM IPSUM DOLOR</h1>
  <p>Lorem ipsum dolor sit amet, consectetur adipisicing elit sed do eiusmod<br>tempor incididunt adipisicing elit sed do eiusmod...</p>
  <span class="hero-rule" style="left:322px"></span>
  <a class="hero-btn" href="#">GET IN TOUCH</a>
  <span class="hero-rule" style="left:505px"></span>
</section>

<section class="steps">
  <div class="step" style="left:158px"><svg width="46" height="46" viewBox="0 0 46 46"><rect x="7" y="7" width="32" height="32" transform="rotate(45 23 23)" fill="none" stroke="#fff" stroke-width="1"/></svg><span class="step-num">1</span><span class="step-label">Select Chosen Product</span></div>
  <div class="step" style="left:293px"><svg width="46" height="46" viewBox="0 0 46 46"><rect x="7" y="7" width="32" height="32" transform="rotate(45 23 23)" fill="none" stroke="#fff" stroke-width="1"/></svg><span class="step-num">2</span><span class="step-label">Input Postcode<br>Distance + Search</span></div>
  <div class="step" style="left:427px"><svg width="46" height="46" viewBox="0 0 46 46"><rect x="7" y="7" width="32" height="32" transform="rotate(45 23 23)" fill="none" stroke="#fff" stroke-width="1"/></svg><span class="step-num">3</span><span class="step-label">Compare<br>Companies + Prices</span></div>
  <div class="step" style="left:563px"><svg width="46" height="46" viewBox="0 0 46 46"><rect x="7" y="7" width="32" height="32" transform="rotate(45 23 23)" fill="none" stroke="#fff" stroke-width="1"/></svg><span class="step-num">4</span><span class="step-label">Contact<br>Chosen Company</span></div>
</section>

<section class="products">
  <div class="product" style="left:158px;top:405px"><div class="product-photo photo-car" role="img" aria-label="White sports car with colourful stickerbomb bonnet"></div><p class="product-title">Colour Change Wrap</p></div>
  <div class="product" style="left:293px;top:405px"><div class="product-photo photo-van" role="img" aria-label="Van with printed vehicle wrap"><span class="plus-h"></span><span class="plus-v"></span><span class="more">More Detail</span></div><p class="product-title">Printed Vehicle Wrap</p></div>
  <div class="product" style="left:427px;top:405px"><div class="product-photo photo-car" role="img" aria-label="White sports car with colourful stickerbomb bonnet"></div><p class="product-title">Window Tint</p></div>
  <div class="product" style="left:563px;top:405px"><div class="product-photo photo-store" role="img" aria-label="Shop front with vinyl lettering on window"></div><p class="product-title">Headlight Tint</p></div>

  <div class="product" style="left:158px;top:563px"><div class="product-photo photo-car" role="img" aria-label="White sports car with colourful stickerbomb bonnet"></div><p class="product-title">Vehicle Signage</p></div>
  <div class="product" style="left:293px;top:563px"><div class="product-photo photo-store" role="img" aria-label="Shop front with vinyl lettering on window"></div><p class="product-title">Shop Signage</p></div>
  <div class="product" style="left:427px;top:563px"><div class="product-photo photo-car" role="img" aria-label="White sports car with colourful stickerbomb bonnet"></div><p class="product-title">Roof Vinyl Wrap</p></div>
  <div class="product" style="left:563px;top:563px"><div class="product-photo photo-bonnet" role="img" aria-label="Silver car with black bonnet wrap seen from above"></div><p class="product-title">Bonnet Vinyl Wrap</p></div>

  <div class="product" style="left:158px;top:723px"><div class="product-photo photo-car" role="img" aria-label="White sports car with colourful stickerbomb bonnet"></div><p class="product-title">Carbon Fibre Vinyl</p></div>
  <div class="product" style="left:293px;top:723px"><div class="product-photo photo-car" role="img" aria-label="White sports car with colourful stickerbomb bonnet"></div><p class="product-title">Stickerbomb Vinyl</p></div>
  <div class="product" style="left:427px;top:723px"><div class="product-photo photo-car" role="img" aria-label="White sports car with colourful stickerbomb bonnet"></div><p class="product-title">Clear Protective Vinyl</p></div>
  <div class="product" style="left:563px;top:723px"><div class="product-photo photo-car" role="img" aria-label="White sports car with colourful stickerbomb bonnet"></div><p class="product-title">Wheel Refurb</p></div>
</section>

<section class="help">
  <h2>HOW CAN WE HELP YOU?</h2>
  <ul>
    <li><svg width="13" height="13" viewBox="0 0 13 13"><circle cx="6.5" cy="6.5" r="6" fill="none" stroke="#fff"/><path d="M3.5 6.5l2 2 4-4" fill="none" stroke="#fff"/></svg>Lorem ipsum dolor sit amet, consectetur<br>dolor sit amet elit sed do eiusmod</li>
    <li><svg width="13" height="13" viewBox="0 0 13 13"><circle cx="6.5" cy="6.5" r="6" fill="none" stroke="#fff"/><path d="M3.5 6.5l2 2 4-4" fill="none" stroke="#fff"/></svg>Lorem ipsum dolor sit amet, consectetur<br>dolor sit amet elit sed do eiusmod</li>
    <li><svg width="13" height="13" viewBox="0 0 13 13"><circle cx="6.5" cy="6.5" r="6" fill="none" stroke="#fff"/><path d="M3.5 6.5l2 2 4-4" fill="none" stroke="#fff"/></svg>Lorem ipsum dolor sit amet, consectetur<br>dolor sit amet elit sed do eiusmod</li>
  </ul>
</section>

<section class="ba" style="left:399px">
  <span class="ba-arrow" style="left:11px"><svg width="10" height="10" viewBox="0 0 10 10"><path d="M6 2.5L3.5 5 6 7.5" fill="none" stroke="#f09d38" stroke-width="1.5"/></svg></span>
  <h3>BEFORE</h3>
  <div class="ba-photo before" role="img" aria-label="Plain white van in a workshop before wrapping"></div>
</section>
<section class="ba" style="left:548px">
  <h3>AFTER</h3>
  <span class="ba-arrow" style="left:124px"><svg width="10" height="10" viewBox="0 0 10 10"><path d="M4 2.5L6.5 5 4 7.5" fill="none" stroke="#f09d38" stroke-width="1.5"/></svg></span>
  <div class="ba-photo after" role="img" aria-label="Same van with red and orange flame printed wrap"></div>
</section>
<a class="click" href="#" style="left:157px">CLICK HERE</a>
<a class="click" href="#" style="left:504px;top:1070px">CLICK HERE</a>

<div class="mascot-spot" role="img" aria-label="Orange mascot peeking over the footer"></div>
<footer class="site-footer">
  <div class="social"><span></span><span></span><span></span></div>
  <p class="footer-links">HOME &nbsp;-&nbsp; BEGINNERS GUIDE &nbsp;-&nbsp; BLOG &nbsp;-&nbsp; CONTACT US &nbsp;-&nbsp; LIST YOUR COMPANY HERE</p>
  <p class="copyright">All Right Resereved Copyright © 2013</p>
</footer>

</body>
</html>
```